New Letterhead request for our Law Firm!

We are a small Estate Planning Firm who just got out logo redesigned. It's attached. We need some letterhead for our client welcome letters and so forth. Clean, bright, and approachable is our style. If you need the specifications for our color scheme or other versions of the logo file, we have those too. Visit our website to get an idea about our services/aesthetics:https://bramblecove.law/

Target Market(s)

Adults 30-80

Colors

Designer to choose colors to be used in the design.

Requirements
Must have
• Logo with color. Contact information

```html
<!DOCTYPE html>
<html lang="en">
<head>
<meta charset="utf-8">
<title>Bramble Cove Law Firm — Letterhead</title>
<link href="https://fonts.googleapis.com/css2?family=Lato:wght@400;700&display=swap" rel="stylesheet">
<style>
  :root{
    --backdrop:#d9cfcc;
    --paper:#fdfdf9;
    --green:#5e8f7c;
    --charcoal:#4a4a4a;
    --ink:#3b3b3b;
  }
  *{margin:0;padding:0;box-sizing:border-box}
  html,body{width:1200px;height:784px;overflow:hidden;background:var(--backdrop)}
  .letterhead{
    position:absolute;left:310px;top:17px;width:580px;height:750px;
    background:var(--paper);box-shadow:0 2px 10px rgba(0,0,0,.12);overflow:hidden;
    font-family:"Lato",sans-serif;color:var(--ink);
  }
  .brand{position:absolute;left:34px;top:30px;display:flex;align-items:center;gap:12px}
  .brand-dot{width:54px;height:54px;border-radius:50%;border:3px solid var(--green)}
  .brand-name{color:var(--green);font-weight:700;text-transform:uppercase;line-height:1.1}
  .brand-name .primary{display:block;font-size:24px;letter-spacing:1.5px}
  .brand-name .secondary{display:block;font-size:12px;letter-spacing:4px}
  .contact{
    position:absolute;right:30px;top:150px;
    border-left:1.5px solid var(--green);padding-left:10px;
    font-size:10.5px;line-height:1.45;
  }
  .contact .firm{color:var(--green);font-weight:700}
  .contact .row{display:flex;align-items:center;gap:6px}
  .contact .row svg{width:9px;height:9px;flex:none}
  .contact .channels{border-top:1px solid var(--green);margin-top:3px;padding-top:2px}
  .footer-wave{position:absolute;left:0;bottom:0;width:580px;height:90px}
</style>
</head>
<body>
<main class="letterhead">
  <header class="brand">
    <span class="brand-dot"></span>
    <span class="brand-name">
      <span class="primary">Bramble Cove</span>
      <span class="secondary">Law Firm</span>
    </span>
  </header>

  <address class="contact" style="font-style:normal">
    <div class="firm">Bramble Cove Law Firm, PLLC</div>
    <div>2450 Linden Ridge Road, Suite 310</div>
    <div>Maple Hollow, MN 55990</div>
    <div class="channels">
      <div class="row">
        <svg viewBox="0 0 10 10" aria-hidden="true"><path d="M2 1l2 2-1 1.2a6 6 0 0 0 2.8 2.8L7 6l2 2-1.3 1.3C4.5 9 1 5.5.7 2.3z" fill="var(--green)"/></svg>
        555-014-2791
      </div>
      <div class="row">
        <svg viewBox="0 0 10 10" aria-hidden="true"><rect x=".5" y="2" width="9" height="6" fill="none" stroke="var(--green)"/><path d="M.5 2l4.5 3.5L9.5 2" fill="none" stroke="var(--green)"/></svg>
        info@bramblecove.law
      </div>
      <div class="row">
        <svg viewBox="0 0 10 10" aria-hidden="true"><circle cx="5" cy="5" r="4.3" fill="none" stroke="var(--green)"/><path d="M.7 5h8.6M5 .7c-2.4 2.6-2.4 6 0 8.6M5 .7c2.4 2.6 2.4 6 0 8.6" fill="none" stroke="var(--green)" stroke-width=".7"/></svg>
        www.bramblecove.law
      </div>
    </div>
  </address>

  <svg class="footer-wave" viewBox="0 0 580 90" aria-hidden="true">
    <path d="M0 30 C150 22 280 58 400 46 S540 26 580 30 L580 90 L0 90 Z" fill="var(--charcoal)"/>
    <path d="M0 20 C150 12 280 48 400 36 S540 16 580 20" fill="none" stroke="var(--green)" stroke-width="3"/>
  </svg>
</main>
</body>
</html>
```